Product label design needed for an odor removal line of products.

I need a label designed for an odor removal product line. There are eight additional odor removal products that I will need labels designed for so the winner will have additional work from me. I would like each of those products to have a similar look and feel in each one. This contest is for one of the products. The Breezeward Pod 385 (would love a better name if you are so inclined -many people know what it is by the 385). The no smell formula does not mask odors, it eliminates odors at their source . Also Reduces Allergens! Simply open silver packet and place in dispenser. Great for use in cars, near pet beds or litter boxes, near diaper pails -anywhere odors are a problem. Lasts 60-90 days. Safe to use. Other uses: Nursing homes, hotel rooms, locker rooms, teenage boy rooms, basements... Eco Friendly! No VOC's or phthalates! Do not consume. Keep out of reach of children and pets. Replace every 60-90 days. I put the picture of my logo , the product as it is packaged and a picture of the actual product and the dispenser it will go in. the package is 4x5 in silver packet with .25 seam on the side and .5 seam on the top and bottom. (Dispenser will have a label with reorder information on it. to be designed later) You do not have to put all information provided on the label. It is to be used as you see fit. I tend to like clean, bold designs but am open to all options. Prefer not to use word air freshener.

Target Market(s)

Men and women between 30-65

Industry/Entity Type

Cleaning Product

Font styles to use
Sans Serif

Colors
acd136
9bcb3c
ffffff

Requirements
Must have
• ability for concept/look to be used for a laundry product, smaller odor elimination pouch, odor removing canister and spray as well
Nice to have
• I like greens but am open to designers to decide
Should not have
• word air freshener

```html
<!DOCTYPE html>
<html lang="en">
<head>
<meta charset="utf-8">
<title>Breezeward Pod 385 – Pouch Label</title>
<link rel="stylesheet" href="https://fonts.googleapis.com/css2?family=Montserrat:wght@600;700;800;900&family=Fira+Sans:wght@500;600&display=swap">
<style>
  :root {
    --canvas: #f2f2f2;
    --teal: #1d6d8d;
    --leaf: #9bcb3c;
    --lime: #acd136;
    --mist: #eef5e6;
    --title-green: #1e9a3c;
    --ink: #1b1b1b;
    --white: #ffffff;
    --orange: #f7941d;
    --orange-edge: #c86a05;
    --photo-tone: #e4e2dc;
  }
  * { box-sizing: border-box; margin: 0; padding: 0; }
  html, body { width: 1200px; height: 1200px; overflow: hidden; }
  body { background: var(--canvas); font-family: "Montserrat", sans-serif; position: relative; }

  .label {
    position: absolute; left: 160px; top: 100px;
    width: 880px; height: 1000px;
    background: linear-gradient(180deg, var(--mist) 27%, #d9ebc4 55%, var(--leaf) 88%, var(--lime) 100%);
    overflow: hidden;
    box-shadow: 0 6px 24px rgba(0,0,0,.15);
  }
  .header-band {
    position: absolute; left: 0; top: 0; width: 100%; height: 271px;
    background: var(--teal);
  }

  .brand {
    position: absolute; left: 50px; top: 40px; width: 210px;
    display: flex; flex-direction: column; align-items: center; gap: 14px;
  }
  .brand-dot { width: 110px; height: 110px; border-radius: 50%; background: var(--leaf); }
  .brand-name {
    font-family: "Montserrat", sans-serif; font-weight: 700; font-size: 26px;
    color: var(--white); letter-spacing: 1px; text-align: center; line-height: 1.1;
  }

  .product-title {
    position: absolute; left: 278px; width: 440px; top: 54px; text-align: center;
  }
  .title-main {
    font-weight: 900; font-size: 50px; line-height: 1; color: var(--title-green);
    letter-spacing: 0.5px;
    text-shadow:
      3px 0 0 var(--white), -3px 0 0 var(--white), 0 3px 0 var(--white), 0 -3px 0 var(--white),
      2px 2px 0 var(--white), -2px -2px 0 var(--white), 2px -2px 0 var(--white), -2px 2px 0 var(--white),
      5px 6px 0 #0b3b2a;
  }
  .title-sub {
    font-weight: 800; font-size: 58px; line-height: 1.05; color: var(--white); margin-top: 12px;
  }
  .title-note {
    font-weight: 700; font-size: 28px; color: var(--white); margin-top: 2px;
  }

  .code-tag {
    position: absolute; left: 734px; top: 38px; width: 125px; height: 87px;
    background: var(--orange); border: 3px solid var(--orange-edge);
    display: flex; align-items: center; justify-content: center;
    font-weight: 800; font-size: 54px; color: var(--ink);
  }

  .formula {
    position: absolute; left: 0; top: 318px; width: 100%; text-align: center; color: var(--ink);
  }
  .formula-head { font-weight: 800; font-size: 41px; line-height: 1.1; }
  .formula-body { font-weight: 600; font-size: 30px; line-height: 1.2; margin-top: 4px; }
  .formula-claim { font-weight: 800; font-size: 41px; line-height: 1.1; margin-top: 6px; }

  .uses-panel {
    position: absolute; left: 40px; top: 540px; width: 480px; height: 312px;
    background: var(--teal); border: 3px solid #cfe6f0;
    padding: 18px 24px; color: var(--white);
    font-family: "Fira Sans", sans-serif; font-weight: 500; font-size: 27px; line-height: 37px;
  }
  .uses-panel h3 { font-family: "Fira Sans", sans-serif; font-weight: 600; font-size: 33px; line-height: 40px; }
  .uses-panel ul { list-style: none; }

  .product-photo {
    position: absolute; left: 536px; top: 530px; width: 323px; height: 250px;
    background: radial-gradient(ellipse at 50% 45%, #fbfaf7 0%, var(--photo-tone) 70%, #cfcdc6 100%);
    border-radius: 10px;
  }

  .how-to {
    position: absolute; left: 536px; top: 796px; width: 312px; height: 106px;
    border-radius: 50%; background: var(--orange); border: 3px solid var(--white);
    display: flex; align-items: center; justify-content: center; text-align: center;
    font-family: "Fira Sans", sans-serif; font-weight: 500; font-size: 20px; line-height: 1.25; color: var(--ink);
  }

  .safety {
    position: absolute; left: 40px; top: 912px; width: 800px;
    font-family: "Fira Sans", sans-serif; font-weight: 600; font-size: 24px; line-height: 36px; color: var(--ink);
  }
</style>
</head>
<body>
  <main class="label">
    <div class="header-band"></div>

    <div class="brand">
      <span class="brand-dot"></span>
      <span class="brand-name">VERDANT HAVEN</span>
    </div>

    <div class="product-title">
      <div class="title-main">BREEZEWARD</div>
      <div class="title-sub">POD</div>
      <div class="title-note">have a given name</div>
    </div>

    <div class="code-tag">385</div>

    <section class="formula">
      <p class="formula-head">THE NO SMELL FORMULA</p>
      <p class="formula-body">does not mask odors, it eliminates odors<br>at their source.</p>
      <p class="formula-claim">ALSO REDUCES ALLERGENS!</p>
    </section>

    <section class="uses-panel">
      <h3>Great for use:</h3>
      <ul>
        <li>- in car</li>
        <li>- near pet beds or litter boxes</li>
        <li>- near diaper pails</li>
        <li>- anywhere odors are a problem.</li>
      </ul>
      <p>Lasts 60-90 days.<br>Safe to use.</p>
    </section>

    <div class="product-photo" role="img" aria-label="Photo of the white odor-eliminating pod pad"></div>

    <div class="how-to">So easy to use<br>simply open silver packet<br>and place in dispenser</div>

    <p class="safety">Eco Friendly! No VOC's or phthalates!<br>Do not consume. Keep out of reach of children and pets.</p>
  </main>
</body>
</html>
```